Want to incorporate elements of all these items to make an amazing sign to welcome people to the community. The sign is 6x4 and needs to incorporate the following items:

Welcome to Thistle Grove

Come visit the DWR sales center at 548 marlow road
High Speed Fiber Internet
Land financing starting at $299 (No credit checks)
Let us build your dream home!
517-384-2296
We like the gold and black design no teal or blue that was another agents design. Some combination of the current sign all the stuff listed above and then design elements that tie into the truck wrap.

Target Market(s)

People visiting the neighborhood

Industry/Entity Type

real estate and construction

Font styles to use
Serif

Colors

Designer to choose colors to be used in the design.

Requirements
Must have
• DWR Home Builders Welcomes you to Thistle Grove, Let us build your dream home, Phone number, Land financing starting at $299 NO credit checks

```html
<!DOCTYPE html>
<html lang="en">
<head>
<meta charset="utf-8">
<title>Welcome to Thistle Grove – Community Sign</title>
<link href="https://fonts.googleapis.com/css2?family=Montserrat:wght@800&family=Roboto:wght@400;700&display=swap" rel="stylesheet">
<style>
  :root {
    --canvas: #5f5f5f;
    --panel: #231f20;
    --gold: #d29a4c;
    --gold-light: #dcaa5e;
    --copper: #a7561b;
    --white: #ffffff;
    --photo-sky: #8e8a6a;
    --photo-field: #b69a6e;
    --photo-green: #4f6b3a;
  }
  * { box-sizing: border-box; margin: 0; padding: 0; }
  html, body { width: 1200px; height: 1110px; overflow: hidden; }
  body { background: var(--canvas); position: relative; font-family: "Roboto", Arial, sans-serif; }

  .sign {
    position: absolute; left: 0; top: 156px;
    width: 1200px; height: 797px;
    background: var(--panel);
    overflow: hidden;
  }
  .sign-header {
    position: absolute; left: 0; top: 0; width: 100%; height: 127px;
    background: linear-gradient(180deg, var(--gold-light) 0%, #c07f3a 50%, var(--copper) 100%);
    display: flex; align-items: center; justify-content: center;
  }
  .sign-title {
    font-family: "Montserrat", Arial, sans-serif; font-weight: 800;
    font-size: 59px; color: var(--white); letter-spacing: 0.5px;
    text-shadow: 0 3px 4px rgba(0,0,0,0.35);
  }
  .sales-center {
    position: absolute; top: 158px; left: 0; width: 100%;
    text-align: center; color: var(--white);
    font-weight: 700; font-size: 37px;
  }
  .feature-icon {
    position: absolute; width: 112px; height: 112px;
    border: 3px solid var(--gold); border-radius: 50%;
    display: flex; align-items: center; justify-content: center;
  }
  .feature-icon svg { width: 60px; height: 60px; }
  .feature-text {
    position: absolute; left: 219px; color: var(--white);
    font-size: 29px; line-height: 43px;
  }
  .tagline {
    position: absolute; left: 63px; top: 563px;
    color: var(--white); font-weight: 700; font-size: 40px;
  }
  .phone-icon {
    position: absolute; left: 65px; top: 653px; width: 80px; height: 80px;
    border: 3px solid var(--gold); border-radius: 50%;
    display: flex; align-items: center; justify-content: center;
  }
  .phone-number {
    position: absolute; left: 175px; top: 650px;
    color: var(--gold); font-weight: 700; font-size: 70px; line-height: 86px;
  }
  .photo-art { position: absolute; left: 0; top: 127px; width: 1200px; height: 670px; }
</style>
</head>
<body>
  <div class="sign">
    <header class="sign-header">
      <h1 class="sign-title">WELCOME TO THISTLE GROVE</h1>
    </header>

    <svg class="photo-art" viewBox="0 127 1200 670" aria-hidden="false">
      <defs>
        <linearGradient id="landscape" x1="0" y1="0" x2="0" y2="1">
          <stop offset="0" stop-color="var(--photo-field)"/>
          <stop offset="0.45" stop-color="var(--photo-green)"/>
          <stop offset="1" stop-color="var(--photo-green)"/>
        </linearGradient>
      </defs>
      <circle class="gold-ring" cx="1053" cy="627" r="380" fill="var(--gold)"/>
      <circle cx="1067" cy="627" r="357" fill="url(#landscape)" role="img"
              aria-label="Photo of hands holding a lot map over a green valley with a highlighted plot"/>
    </svg>

    <p class="sales-center">Come visit the DWR sales center at 548 marlow road</p>

    <div class="feature-icon" style="left:69px; top:261px;">
      <svg viewBox="0 0 60 60" fill="none" stroke="#fff" stroke-width="2.5" stroke-linecap="round">
        <path d="M8 16 C20 20 28 28 34 34"/>
        <path d="M8 26 C18 28 26 34 30 42"/>
        <path d="M12 38 C18 40 22 44 24 50"/>
        <circle cx="38" cy="36" r="3"/><circle cx="46" cy="30" r="3"/>
        <circle cx="46" cy="42" r="3"/><circle cx="34" cy="46" r="3"/>
      </svg>
    </div>
    <p class="feature-text" style="top:293px;">High Speed Fiber Internet</p>

    <div class="feature-icon" style="left:69px; top:407px;">
      <svg viewBox="0 0 60 60" fill="none" stroke="#fff" stroke-width="2.5" stroke-linejoin="round">
        <path d="M30 38 C20 28 18 22 18 18 A12 12 0 0 1 42 18 C42 22 40 28 30 38 Z"/>
        <path d="M34 13 H28 A3 3 0 0 0 28 19 H32 A3 3 0 0 1 32 25 H26 M30 10 V28" stroke-width="2"/>
        <path d="M8 46 L30 36 L52 46 L30 56 Z"/>
        <path d="M19 41 L41 51 M41 41 L19 51"/>
      </svg>
    </div>
    <p class="feature-text" style="top:418px;">Land financing starting at<br>$299 (No credit checks)</p>

    <p class="tagline">Let us build your dream home!</p>

    <div class="phone-icon">
      <svg width="40" height="40" viewBox="0 0 24 24" fill="var(--gold)">
        <path d="M6.6 10.8a15.1 15.1 0 0 0 6.6 6.6l2.2-2.2c.3-.3.7-.4 1-.2 1.1.4 2.3.6 3.6.6.6 0 1 .4 1 1V20c0 .6-.4 1-1 1A17 17 0 0 1 3 4c0-.6.4-1 1-1h3.5c.6 0 1 .4 1 1 0 1.3.2 2.5.6 3.6.1.3 0 .7-.2 1l-2.3 2.2z"/>
      </svg>
    </div>
    <p class="phone-number">517-384-2296</p>
  </div>
</body>
</html>
```